Selka Marrow Photography Business Card

I need a new business card/ possibly design to use for other marking materials ... I have included my logo below in a few different colors, but can also provide the logo in additional colors and sizes. I would love a card the expresses clean, simple and classy.

Target Market(s)

Portrait photography clients, child photography clients

Industry/Entity Type

Photographer

Contact Information for Business Card

Selka Marrow Photography, Alderbrook MA, www.selkamarrowphotography.example
T. 555-283-9146 E. selkamarrowphoto@mailbox.example

Colors
33b8a4
eea4c8
5c5c5c

Requirements
Must have
• I would like to include my logo on card.
Nice to have
• I also like the color brown as well as the choices below. I would like a simple, elegant card, something classy.

```html
<!DOCTYPE html>
<html lang="en">
<head>
<meta charset="utf-8">
<title>Selka Marrow Photography – Business Card</title>
<link rel="stylesheet" href="https://fonts.googleapis.com/css2?family=Montserrat:wght@400;500;600&family=Courgette&display=swap">
<style>
  :root {
    --teal: #5fb8aa;
    --ink: #5c5c5c;
    --ink-soft: #8a8a8a;
    --paper: #ffffff;
    --backdrop: #d9d9d9;
    --photo-top: #8d8590;
    --photo-mid: #b08a63;
    --photo-low: #2f2a28;
  }
  * { margin: 0; padding: 0; box-sizing: border-box; }
  html, body { width: 1200px; height: 900px; overflow: hidden; }
  body {
    background: var(--backdrop);
    font-family: "Montserrat", sans-serif;
    position: relative;
  }
  .card {
    position: absolute;
    top: 165px;
    width: 325px;
    height: 570px;
    background: var(--paper);
    box-shadow: 0 2px 6px rgba(0,0,0,0.18);
  }
  .card-front { left: 265px; text-align: center; }
  .card-back { left: 611px; }

  .brand-mark {
    position: absolute;
    top: 60px;
    left: 0; right: 0;
    color: var(--teal);
    font-size: 11px;
    font-weight: 600;
    letter-spacing: 2.5px;
    text-transform: uppercase;
  }
  .owner-name {
    position: absolute;
    top: 282px;
    left: 0; right: 0;
    font-family: "Courgette", cursive;
    font-weight: 400;
    font-size: 36px;
    line-height: 1;
    color: var(--teal);
  }
  .owner-role {
    position: absolute;
    top: 325px;
    left: 0; right: 0;
    font-size: 12px;
    font-weight: 500;
    letter-spacing: 1.2px;
    color: var(--ink);
  }
  .contact {
    position: absolute;
    left: 0; right: 0;
    font-size: 11.5px;
    letter-spacing: 1.6px;
    color: var(--ink-soft);
    line-height: 23px;
  }
  .contact-phone { top: 382px; }
  .contact-web { top: 492px; font-size: 10.5px; letter-spacing: 1.3px; }

  .portrait {
    position: absolute;
    top: 22px;
    left: 18px;
    width: 286px;
    height: 525px;
    background: linear-gradient(180deg, var(--photo-top) 0%, var(--photo-mid) 25%, #6e5d52 45%, var(--photo-low) 75%, #3a3432 100%);
  }
</style>
</head>
<body>
  <section class="card card-front" aria-label="Business card front">
    <div class="brand-mark">Selka Marrow Photography</div>
    <h1 class="owner-name">selka marrow</h1>
    <p class="owner-role">PHOTOGRAPER</p>
    <p class="contact contact-phone">555-283-9146<br>Alderbrook MA</p>
    <p class="contact contact-web">selkamarrowphoto@mailbox.example<br>www.selkamarrowphotography.example</p>
  </section>

  <section class="card card-back" aria-label="Business card back">
    <div class="portrait" role="img" aria-label="Portrait photograph of a young woman in a winter coat with a fur-trimmed hood, sitting by a birch tree in snow"></div>
  </section>
</body>
</html>
```